Boutique Wealth management firm needs a new business card design

I want to update my business card design to be more consistent with the look and feel of my website (www.corvalen-capital.example). I would like to incorporate an ivory parchment background and am open to switching from the current "portrait" layout to a more traditional "landscape" orientation. The final design should convey stability and exclusivity and I want something in PDF format that is ready to send to the printer
Updates

Thank you all for taking the time to submit your designs for my project. I've made my decision and picked the design I like best. Thanks again!

Industry/Entity Type

Business

```html
<!DOCTYPE html>
<html lang="en">
<head>
<meta charset="utf-8">
<title>Corvalen Capital Advisory – Business Card</title>
<link rel="stylesheet" href="https://fonts.googleapis.com/css2?family=Lato:wght@400;700;900&display=swap">
<style>
  :root {
    --backdrop: #2b2b2d;
    --parchment-light: #f3e4b4;
    --parchment-mid: #e9d59c;
    --parchment-dark: #d9c184;
    --maroon: #6b2a45;
    --ink: #1d1a16;
  }
  * { box-sizing: border-box; margin: 0; padding: 0; }
  html, body {
    width: 1200px; height: 1000px; overflow: hidden;
    background: var(--backdrop);
    font-family: "Lato", sans-serif;
  }
  .canvas {
    width: 1200px; height: 1000px;
    display: flex; align-items: center; justify-content: center;
  }
  .business-card {
    position: relative;
    width: 900px; height: 514px;
    background:
      radial-gradient(ellipse at 30% 35%, var(--parchment-light) 0%, transparent 60%),
      radial-gradient(ellipse at 75% 70%, var(--parchment-light) 0%, transparent 55%),
      linear-gradient(135deg, var(--parchment-mid) 0%, var(--parchment-dark) 100%);
    box-shadow: 0 10px 0 var(--maroon), 0 24px 40px rgba(0,0,0,.45);
    color: var(--ink);
  }
  .firm-name {
    position: absolute; left: 62px; top: 196px;
    color: var(--maroon);
    font-weight: 900; font-size: 46px; line-height: 1.05;
    letter-spacing: 1px;
  }
  .contact-block {
    position: absolute; left: 500px; top: 58px; width: 370px;
  }
  .person-name {
    color: var(--maroon); font-weight: 900; font-size: 30px;
  }
  .person-title {
    font-weight: 700; font-size: 19px; margin-top: 6px; margin-left: 12px;
  }
  .contact-list {
    list-style: none; margin-top: 26px; margin-left: 36px;
  }
  .contact-list li {
    display: flex; align-items: center; gap: 12px;
    font-size: 21px; line-height: 32px;
  }
  .contact-list svg { width: 22px; height: 22px; fill: var(--maroon); flex: none; }
  .mailing-address {
    margin-top: 30px; margin-left: 56px;
    font-size: 21px; line-height: 27px; font-style: normal;
  }
  .mailing-address strong { font-weight: 900; }
  .license-line {
    position: absolute; left: 610px; top: 430px;
    font-size: 20px;
  }
</style>
</head>
<body>
<main class="canvas">
  <section class="business-card">
    <h1 class="firm-name">CORVALEN<br>Capital Advisory</h1>

    <div class="contact-block">
      <h2 class="person-name">Dana Whitford, CFP®</h2>
      <p class="person-title">Principal</p>

      <ul class="contact-list">
        <li>
          <svg viewBox="0 0 24 24" aria-hidden="true"><path d="M6.6 10.8a15.1 15.1 0 0 0 6.6 6.6l2.2-2.2a1 1 0 0 1 1-.25 11.4 11.4 0 0 0 3.6.57 1 1 0 0 1 1 1V20a1 1 0 0 1-1 1A17 17 0 0 1 3 4a1 1 0 0 1 1-1h3.5a1 1 0 0 1 1 1c0 1.25.2 2.45.57 3.57a1 1 0 0 1-.25 1z"/></svg>
          <span>925-555-0148</span>
        </li>
        <li>
          <svg viewBox="0 0 24 24" aria-hidden="true"><path d="M2 5h20v14H2z M4 7v.5l8 5 8-5V7l-8 5z" fill-rule="evenodd"/></svg>
          <span>dana@corvalen-capital.example</span>
        </li>
        <li>
          <svg viewBox="0 0 24 24" aria-hidden="true"><path d="M12 2a10 10 0 1 0 0 20 10 10 0 0 0 0-20zm-1 17.9A8 8 0 0 1 4 12l5 5v1a2 2 0 0 0 2 2zm6.9-2.5A2 2 0 0 0 16 16h-1v-3a1 1 0 0 0-1-1H8v-2h2a1 1 0 0 0 1-1V7h2a2 2 0 0 0 2-2v-.4a8 8 0 0 1 2.9 12.8z"/></svg>
          <span>www.corvalen-capital.example</span>
        </li>
      </ul>

      <address class="mailing-address">
        <strong>Mailing Address:</strong><br>
        2180 Alder Crest Rd. #214<br>
        Fairmont, CA 94500
      </address>
    </div>

    <p class="license-line">CA Insurance License #0K71836</p>
  </section>
</main>
</body>
</html>
```